Redesign my business cards

I would like pretty much all the same information as my current business cards but redesigned to stand out more and be more unique photo uploaded to show my current business cards don’t mind if you want to remove or replace I for on the back

```html
<!DOCTYPE html>
<html lang="en">
<head>
<meta charset="utf-8">
<title>Tidewell Detailing – Business Card</title>
<link rel="stylesheet" href="https://fonts.googleapis.com/css2?family=Montserrat:wght@400;500;600;700&display=swap">
<style>
  :root {
    --backdrop: #29292b;
    --card: #8dd5f1;
    --ink: #1a64a8;
    --ink-dark: #0e5a9e;
    --ink-soft: #3d77ae;
  }
  * { box-sizing: border-box; margin: 0; padding: 0; }
  html, body {
    width: 1200px; height: 800px; overflow: hidden;
    background: var(--backdrop);
    font-family: "Montserrat", Arial, sans-serif;
  }
  .sheet {
    width: 1200px; height: 800px;
    display: flex; align-items: center; justify-content: center; gap: 36px;
  }
  .card {
    width: 546px; height: 340px;
    background: var(--card);
    color: var(--ink);
    position: relative;
    overflow: hidden;
    box-shadow: 0 12px 32px rgba(0,0,0,.5);
  }

  /* Front */
  .card--front { padding: 34px 38px; }
  .card--front .brand {
    display: flex; align-items: center; gap: 14px;
  }
  .brand-mark {
    width: 72px; height: 72px; border-radius: 50%;
    background: var(--ink-dark); flex: none;
  }
  .brand-name {
    font-weight: 700; font-size: 16px; letter-spacing: .1em;
    color: var(--ink-dark); text-transform: uppercase; line-height: 1.3;
  }
  .person { margin-top: 24px; }
  .person-name {
    font-weight: 600; font-size: 38px; letter-spacing: .01em;
    color: var(--ink-dark); text-transform: uppercase; line-height: 1;
  }
  .person-role {
    margin-top: 8px; font-size: 12px; letter-spacing: .55em;
    font-weight: 500; text-transform: uppercase;
  }
  .contact {
    margin-top: 18px; font-weight: 500; font-size: 19px; line-height: 1.6;
    color: var(--ink-dark);
  }

  /* Back */
  .card--back { display: flex; padding: 26px 26px 22px 26px; gap: 22px; }
  .card--back .brand {
    width: 150px; flex: none;
    display: flex; flex-direction: column; align-items: center; justify-content: center; gap: 14px;
    text-align: center;
  }
  .card--back .brand-mark { width: 104px; height: 104px; }
  .card--back .brand-name { font-size: 15px; }
  .services { flex: 1; display: flex; flex-direction: column; justify-content: space-between; }
  .service-title { font-weight: 600; font-size: 15px; color: var(--ink-dark); margin-bottom: 4px; }
  .service-list { list-style: none; font-size: 10px; line-height: 1.45; color: var(--ink-soft); }
</style>
</head>
<body>
<main class="sheet">

  <section class="card card--front" aria-label="Card front">
    <div class="brand">
      <span class="brand-mark"></span>
      <span class="brand-name">Tidewell<br>Detailing</span>
    </div>
    <div class="person">
      <h1 class="person-name">Owen Marsh</h1>
      <p class="person-role">Owner</p>
    </div>
    <div class="contact">
      <p>M: 0400555012</p>
      <p>E : tidewelldetailing@example.com</p>
    </div>
  </section>

  <section class="card card--back" aria-label="Card back">
    <div class="brand">
      <span class="brand-mark"></span>
      <span class="brand-name">Tidewell<br>Detailing</span>
    </div>
    <div class="services">
      <article class="service">
        <h2 class="service-title">Interior Detail - $150</h2>
        <ol class="service-list">
          <li>1. Vacume &amp; deep clean of carpets &amp; upholstery</li>
          <li>2. Interior trim or leather clean &amp; condition</li>
          <li>3. Window polish and treatment</li>
          <li>4. Steam clean and stain removal</li>
        </ol>
      </article>
      <article class="service">
        <h2 class="service-title">Exterior Detail - $250</h2>
        <ol class="service-list">
          <li>1. Extreme wash &amp; polish</li>
          <li>2. Exterior trim reviver &amp; protector</li>
          <li>3. Window polish &amp; treatment</li>
          <li>4. Tyre dressing, engine bay cleaned</li>
        </ol>
      </article>
      <article class="service">
        <h2 class="service-title">Full Extreme Detail - $350</h2>
        <ol class="service-list">
          <li>1. Extreme wash &amp; polish,</li>
          <li>2. Exterior trim reviver &amp; protector</li>
          <li>3. Window polish &amp; treatment</li>
          <li>4. Tyre dressing, engine bay cleaned</li>
        </ol>
      </article>
    </div>
  </section>

</main>
</body>
</html>
```